wealth management firm, professional group, new model

we have a logo that works but we need a card, white background using our colors...clean look

our tag line if can be used in

Guiding Every Client Toward Ownership

```html
<!DOCTYPE html>
<html lang="en">
<head>
<meta charset="utf-8">
<title>Alden Wealth Partners – Business Card</title>
<link rel="stylesheet" href="https://fonts.googleapis.com/css2?family=Montserrat:wght@400;500;800&display=swap">
<style>
  :root {
    --stage: #1d1d1f;
    --navy: #0f2557;
    --navy-back: #1b2d4f;
    --ink: #1c1c28;
    --paper: #fdfdfd;
    --white: #ffffff;
  }
  * { margin: 0; padding: 0; box-sizing: border-box; }
  html, body {
    width: 1200px; height: 1059px; overflow: hidden;
    background: var(--stage);
    font-family: "Montserrat", sans-serif;
  }
  .card {
    position: absolute; left: 245px;
    width: 710px; height: 405px;
    border-radius: 41px; overflow: hidden;
  }
  .card-front { top: 84px; background: var(--paper); }
  .card-back { top: 552px; background: var(--navy-back); }

  .front-shapes { position: absolute; inset: 0; }

  .person { position: absolute; left: 44px; top: 104px; }
  .person-name {
    font-weight: 800; font-size: 31px; color: var(--navy);
    letter-spacing: 0.3px; line-height: 1;
  }
  .person-title {
    margin-top: 8px; font-weight: 400; font-size: 18.5px;
    color: var(--ink); letter-spacing: 1.2px; line-height: 1;
  }
  .title-rule {
    position: absolute; left: 46px; top: 186px;
    width: 70px; height: 3px; background: var(--navy);
  }

  .contact-list { position: absolute; left: 46px; top: 212px; list-style: none; }
  .contact-item {
    display: flex; align-items: center; height: 26px; margin-bottom: 17px;
  }
  .contact-icon { width: 25px; height: 25px; flex: none; }
  .contact-divider {
    width: 2px; height: 23px; background: var(--navy); margin: 0 19px 0 18px;
  }
  .contact-text { font-size: 14.5px; color: var(--ink); letter-spacing: 0.5px; }

  .brand-block {
    position: absolute; left: 415px; width: 264px; top: 170px;
    text-align: center; color: var(--navy);
  }
  .brand-name {
    font-weight: 500; font-size: 21px; line-height: 1.2;
    white-space: nowrap;
  }
  .address {
    margin-top: 34px; font-size: 13.5px; line-height: 20px;
    color: var(--ink); letter-spacing: 0.2px;
  }

  .back-content {
    position: absolute; inset: 0;
    display: flex; flex-direction: column; align-items: center;
  }
  .back-brand {
    margin-top: 165px; color: var(--white); font-weight: 500;
    font-size: 32px; line-height: 1; white-space: nowrap;
  }
  .tagline {
    margin-top: 88px; color: var(--white); font-size: 22px;
    font-weight: 400; letter-spacing: 0.3px;
  }
</style>
</head>
<body>

<section class="card card-front">
  <svg class="front-shapes" width="710" height="405" viewBox="0 0 710 405" aria-hidden="true">
    <rect width="710" height="405" fill="var(--navy)"/>
    <path d="M162,0 C68,0 0,62 0,160 L0,328 C14,360 45,375 92,375 L345,375 C380,375 402,388 418,405 L710,405 L710,0 Z" fill="var(--paper)"/>
    <circle cx="611" cy="204" r="254" fill="var(--paper)" stroke="var(--navy)" stroke-width="5"/>
  </svg>

  <div class="person">
    <h1 class="person-name">DANIEL HART</h1>
    <p class="person-title">MANAGING DIRECTOR</p>
  </div>
  <div class="title-rule"></div>

  <ul class="contact-list">
    <li class="contact-item">
      <svg class="contact-icon" viewBox="0 0 24 24" aria-hidden="true">
        <circle cx="12" cy="12" r="12" fill="var(--navy)"/>
        <path d="M8.2 6.5l2 2.4-1.2 1.5c.8 1.7 2 2.9 3.6 3.7l1.5-1.2 2.4 2-1.2 1.9c-4.3-.4-8.3-4.4-8.8-8.8z" fill="var(--white)"/>
      </svg>
      <span class="contact-divider"></span>
      <span class="contact-text">044-555 010 234</span>
    </li>
    <li class="contact-item">
      <svg class="contact-icon" viewBox="0 0 24 24" aria-hidden="true">
        <circle cx="12" cy="12" r="12" fill="var(--navy)"/>
        <rect x="6" y="7.5" width="12" height="9" rx="1" fill="var(--white)"/>
        <path d="M6.5 8.2l5.5 4.3 5.5-4.3" fill="none" stroke="var(--navy)" stroke-width="1.1"/>
      </svg>
      <span class="contact-divider"></span>
      <span class="contact-text">info@mailname.com</span>
    </li>
    <li class="contact-item">
      <svg class="contact-icon" viewBox="0 0 24 24" aria-hidden="true">
        <circle cx="12" cy="12" r="12" fill="var(--navy)"/>
        <circle cx="12" cy="12" r="6.5" fill="none" stroke="var(--white)" stroke-width="1.3"/>
        <ellipse cx="12" cy="12" rx="2.8" ry="6.5" fill="none" stroke="var(--white)" stroke-width="1.1"/>
        <path d="M5.5 12h13" stroke="var(--white)" stroke-width="1.1"/>
      </svg>
      <span class="contact-divider"></span>
      <span class="contact-text">www.sitename.com</span>
    </li>
  </ul>

  <div class="brand-block">
    <p class="brand-name">Alden Wealth Partners</p>
    <p class="address">421, Address line goes here<br>45452, Country name</p>
  </div>
</section>

<section class="card card-back">
  <div class="back-content">
    <p class="back-brand">Alden Wealth Partners</p>
    <p class="tagline">Guiding Every Client Toward Ownership</p>
  </div>
</section>

</body>
</html>
```